Birch Coach Rental Club (motorhome) rental club needs a web desin

The name of our club is Birch Coach Rental Club. I am looking for a web site that will show our motorhomes.
It needs to let us add motorhomes and change descriptions etc. (back end functionality)
It needs to show an RV with a description, with a calendar of availability for each RV.
It needs to allow club members the ability to schedule and pay for an RV. (ecommerce)
It needs a page where new members can go to join the club.
check out this link for an idea of how I would like the RVs presented. http://www.velmorawingschool.example/Aircraft.html
We are an RV (motor home) rental club. Birchcoachrentalclub.example.
Needed is one cohesive design which will be used for more than 1 page. I need the web site to:
1. show our RV's for rent.
It must show a picture with details about the RV, (image placeholder for now – can possible give picture with details about the RV later on to the winning designer)
....with a link to the calendar for that RV which must allow a club member to pick the dates they want (the calendar must block them from picking dates that have been reserved or are less than the minimum days allowed for that time period (3 days low season and 5 days high season) the amounts for this must be changeable by us, a dollar amount for each day, week or month. This they will put in their shopping cart which must calculate a total and allow them to delete items. It also must allow them to put down a deposit if more than 30 days out or
pay 100% if under 30 days. There needs to be a link to extras they can add to the cart such as linens, kitchenware, delivery service, pickup service, dump charge, fuel charge, propane charge etc. This is a separate page good for all Rv's There needs to be a link to more pictures.
2. There needs to be a members area that they can log into with a user name
and a password that show their passed rentals and up coming rentals.
3 There needs to be a new members area that allows them to input their information, name, address, credit card, etc., agree to the rules of the club. This is where they will create there user name a password.
4. There needs to be an administrator area that shows a list of the RVs a
calendar for each with the dates that are taken. The area needs to show the
deposits received the rents received, there needs to be a reports area the
will show revenue received by dates picked. It needs to let's us take the
RV offline for repairs Etc. (back end)
5. Needs to be away to track sales tax. (This could be part of the reports
area)
6. There needs to be a "how it works tab".
7. An “about us” tab.
8. There needs to be a way to add new RVs and make other changes as needed. (back end)
Thanks, Lou Fenner

```html
<!DOCTYPE html>
<html lang="en">
<head>
<meta charset="utf-8">
<title>Birch Coach Rental Club</title>
<link href="https://fonts.googleapis.com/css2?family=Open+Sans:wght@400;600;700&display=swap" rel="stylesheet">
<style>
:root{
  --sky:#4fb8ec;
  --sky-deep:#2a9fe0;
  --sky-light:#8fd3f6;
  --orange:#f7941d;
  --orange-light:#ffc21a;
  --ink:#333a40;
  --muted:#777;
  --line:#dcdcdc;
  --gray-bg:#f1f1f1;
  --white:#fff;
}
*{box-sizing:border-box;margin:0;padding:0}
html,body{width:1200px;height:2830px;overflow:hidden}
body{font-family:"Open Sans",Arial,sans-serif;color:var(--ink);background:var(--white);position:relative}
a{color:inherit;text-decoration:none}

.site-header{position:absolute;top:0;left:0;width:1200px;height:106px;background:linear-gradient(#fff,#f2f2f2)}
.brand{position:absolute;left:132px;top:26px;display:flex;align-items:center;gap:18px}
.brand-mark{width:56px;height:52px;border-radius:10px;background:var(--sky)}
.brand-name{font-size:25px;font-weight:700;color:#3a3f44}
.header-contact{position:absolute;top:36px;display:flex;align-items:center;gap:12px;font-size:15px;color:#444}
.header-contact .ico{width:32px;height:32px;border-radius:50%;background:var(--sky);display:flex;align-items:center;justify-content:center}
.hc-phone{left:717px}.hc-mail{left:887px}

.main-nav{position:absolute;top:106px;left:0;width:1200px;height:42px;background:linear-gradient(var(--sky-light),var(--sky));border-top:1px solid #7cc9f1}
.main-nav ul{list-style:none;display:flex;position:absolute;left:132px;top:0;height:42px}
.main-nav li{font-size:12px;color:#fff;padding:0 17px;line-height:42px}
.main-nav li.active{background:linear-gradient(var(--orange-light),var(--orange));}

.hero{position:absolute;top:148px;left:0;width:1200px;height:437px;background:linear-gradient(160deg,#bcd3df 0%,#8aa5b2 25%,#5b6d63 45%,#8a8d80 60%,#3f4d4f 80%,#6d7c80 100%)}
.hero-title{position:absolute;left:132px;top:36px;font-size:31px;font-weight:700;color:#fff;line-height:36px;text-shadow:0 2px 3px rgba(0,0,0,.45)}
.join-card{position:absolute;left:132px;top:127px;width:270px;height:250px;background:linear-gradient(var(--orange-light),var(--orange));padding:18px 20px}
.join-card h2{font-size:18px;font-weight:700;color:#fff;margin-bottom:16px}
.field{height:36px;background:#fff;margin-bottom:6px;border-radius:2px;display:flex;align-items:center;gap:12px;padding-left:12px;font-size:12px;color:#333}
.field svg{flex:none}
.btn-join{display:inline-block;margin-top:14px;background:#2b2b2b;color:#fff;font-size:13px;font-weight:700;padding:8px 12px;border-radius:3px}
.hero-dots{position:absolute;left:132px;top:398px;display:flex;gap:6px}
.hero-dots span{width:6px;height:6px;border-radius:50%;background:#fff;opacity:.7}
.hero-dots span:first-child{opacity:1}

.features{position:absolute;top:585px;left:0;width:1200px;height:217px;background:linear-gradient(var(--sky-light),var(--sky))}
.feature{position:absolute;top:45px;width:300px}
.feature .thumb{position:absolute;left:0;top:0;width:100px;height:92px;border:3px solid #fff;background:linear-gradient(#cfe3ee,#8aa0a6)}
.feature h3{position:absolute;left:120px;top:-6px;font-size:24px;font-weight:700;color:#fff;line-height:32px;width:190px}
.feature p{position:absolute;left:120px;top:72px;width:186px;font-size:11px;line-height:20px;color:#eaf7ff;text-align:justify}
.f1{left:132px}.f2{left:455px}.f3{left:777px}

.catalog{position:absolute;top:802px;left:0;width:1200px;height:1683px;background:linear-gradient(#e9e9e9,#fff 120px)}
.catalog h2{position:absolute;left:132px;top:38px;font-size:23px;font-weight:700;color:#333}
.rv-card{position:absolute;left:132px;width:936px;height:275px;background:linear-gradient(#fff,#f4f4f4);border:1px solid var(--line)}
.specs{position:absolute;left:15px;top:15px;width:193px;height:242px;background:linear-gradient(var(--sky-light),var(--sky));padding:14px 0 0 11px;color:#fff}
.specs h4{font-size:17px;font-weight:700;margin-bottom:8px}
.specs dl{display:grid;grid-template-columns:102px 1fr;font-size:10.5px;line-height:19px}
.rv-photo{position:absolute;left:236px;top:22px;width:368px;height:230px;background:linear-gradient(#ffffff,#ececec 60%,#d8d8d8);border-radius:4px}
.rv-info{position:absolute;left:623px;top:28px;width:297px}
.rv-info h3{font-size:18px;font-weight:700;color:var(--sky-deep)}
.price{margin-top:10px;font-size:24px;font-weight:700;color:var(--orange)}
.price small{font-size:11px;font-weight:400;color:var(--sky-deep);margin-left:10px}
.rv-info p{margin-top:6px;font-size:11.5px;line-height:22.5px;color:#555;text-align:justify}
.actions{margin-top:16px;display:flex;gap:8px}
.btn{width:103px;height:36px;font-size:11px;color:#fff;display:flex;align-items:center;justify-content:center;border-radius:2px}
.btn-sky{background:linear-gradient(var(--sky-light),var(--sky-deep))}
.btn-orange{background:linear-gradient(var(--orange-light),var(--orange))}

.pager{position:absolute;left:708px;top:1622px;display:flex;gap:6px;list-style:none}
.pager li{min-width:24px;height:24px;padding:0 6px;border:1px solid #ccc;background:#f6f6f6;font-size:10px;display:flex;align-items:center;justify-content:center;color:#444}
.pager li.wide{padding:0 10px}

.site-footer{position:absolute;top:2485px;left:0;width:1200px;height:345px;background:linear-gradient(var(--sky-light),var(--sky));color:#fff}
.f-col{position:absolute;top:40px}
.f-col h5{font-size:19px;font-weight:700;margin-bottom:14px}
.f-links{list-style:none;font-size:11px;line-height:22.5px}
.f-news{left:340px;width:230px}
.f-news p{font-size:11px;line-height:22px;color:#e8f6ff}
.mail-input{margin-top:22px;width:206px;height:42px;background:#fff;display:flex;align-items:center;gap:10px;padding-left:14px;font-size:10px;color:#444}
.btn-sub{display:inline-block;margin-top:22px;background:linear-gradient(var(--orange-light),var(--orange));font-size:10px;padding:8px 12px;border-radius:2px}
.f-contact{left:668px;width:230px;font-size:11px;line-height:22px}
.f-contact .row{display:flex;gap:14px;margin-bottom:8px}
.f-follow{left:960px;width:110px}
.f-follow h5{text-align:right}
.social{display:flex;align-items:center;gap:12px;margin-bottom:10px;font-size:11px}
.social .dot{width:34px;height:34px;border-radius:50%;border:2px solid #fff;flex:none}
.legal{position:absolute;top:2768px;left:132px;width:936px;border-top:1px solid rgba(255,255,255,.45);display:flex;justify-content:space-between;padding-top:12px;font-size:11px;color:#fff}
</style>
</head>
<body>

<header class="site-header">
  <div class="brand"><span class="brand-mark"></span><span class="brand-name">Birch Coach Rental Club</span></div>
  <div class="header-contact hc-phone"><span class="ico"><svg width="14" height="14" viewBox="0 0 24 24"><path fill="#fff" d="M6.6 10.8a15 15 0 0 0 6.6 6.6l2.2-2.2c.3-.3.7-.4 1-.2 1.1.4 2.3.6 3.6.6.6 0 1 .4 1 1V20c0 .6-.4 1-1 1A17 17 0 0 1 3 4c0-.6.4-1 1-1h3.5c.6 0 1 .4 1 1 0 1.3.2 2.5.6 3.6.1.3 0 .7-.2 1z"/></svg></span>1-(555) 014-2290</div>
  <div class="header-contact hc-mail"><span class="ico"><svg width="14" height="14" viewBox="0 0 24 24"><path fill="#fff" d="M3 5h18v14H3z"/><path fill="none" stroke="#4fb8ec" stroke-width="2" d="M3 6l9 7 9-7"/></svg></span>hello@birchcoach.example</div>
</header>

<nav class="main-nav">
  <ul>
    <li class="active">Home</li><li>RV Rentals</li><li>Specials</li><li>Policies</li><li>Reviews</li><li>Blog</li><li>Contact &amp; Location</li><li>Request Quote</li>
  </ul>
</nav>

<section class="hero" role="img" aria-label="Photo of a white motorhome driving a coastal road beside mountains and sea">
  <h1 class="hero-title">Enjoy a dream holiday<br>in Crete.</h1>
  <form class="join-card">
    <h2>Birch Coach Rental Club</h2>
    <div class="field"><svg width="11" height="11" viewBox="0 0 24 24"><circle cx="12" cy="7" r="5" fill="#333"/><path d="M2 23c0-6 4-9 10-9s10 3 10 9z" fill="#333"/></svg>Name</div>
    <div class="field"><svg width="11" height="11" viewBox="0 0 24 24"><rect x="2" y="5" width="20" height="14" fill="#333"/><path d="M2 6l10 7 10-7" fill="none" stroke="#fff" stroke-width="2"/></svg>Email</div>
    <div class="field"><svg width="11" height="11" viewBox="0 0 24 24"><rect x="4" y="10" width="16" height="12" fill="#333"/><path d="M7 10V7a5 5 0 0 1 10 0v3" fill="none" stroke="#333" stroke-width="3"/></svg>Password</div>
    <span class="btn-join">Join Now</span>
  </form>
  <div class="hero-dots"><span></span><span></span><span></span></div>
</section>

<section class="features">
  <div class="feature f1"><div class="thumb" role="img" aria-label="Photo of a motorhome parked outdoors"></div><h3>Enjoy a dream holiday</h3><p>Neque porro quisquam est, qui dolorem ipsum quia dolor sit amet, consectetur.</p></div>
  <div class="feature f2"><div class="thumb" role="img" aria-label="Photo of a lake and hills"></div><h3>Check Our Special Offers</h3><p>Neque porro quisquam est, qui dolorem ipsum quia dolor sit amet, consectetur.</p></div>
  <div class="feature f3"><div class="thumb" role="img" aria-label="Photo of a camper on a mountain road"></div><h3>24/7 Tech Support</h3><p>Neque porro quisquam est, qui dolorem ipsum quia dolor sit amet, consectetur.</p></div>
</section>

<main class="catalog">
  <h2>Our Motorhomes</h2>

  <article class="rv-card" style="top:108px">
    <div class="specs"><h4>SpecificationS</h4><dl><dt>Mileage:</dt><dd>27</dd><dt>Fuel:</dt><dd>Diesel</dd><dt>Transmission:</dt><dd>Manual</dd><dt>Colour:</dt><dd>White</dd><dt>Berths:</dt><dd>5</dd><dt>Belts:</dt><dd>4</dd><dt>Engine Power:</dt><dd>150 BHP</dd><dt>Length:</dt><dd>7,530</dd><dt>Width:</dt><dd>2,270</dd></dl></div>
    <div class="rv-photo" role="img" aria-label="Photo of a white coachbuilt motorhome"></div>
    <div class="rv-info"><h3>2016 Camper Van 150 BHP</h3><div class="price">$150<small>Per Day</small></div><p>Low Profile, Cab Air Conditioning, Swivel Driver/passenger Seat, Cruise Control, Central Locking, Fine Wood Dashboard Inlays, Rear Garage, Vento Toilet Ventilation, Dvb-t Radio/dvd</p><div class="actions"><span class="btn btn-sky">Schedule Now</span><span class="btn btn-orange">Join the Club</span></div></div>
  </article>

  <article class="rv-card" style="top:408px">
    <div class="specs"><h4>SpecificationS</h4><dl><dt>Mileage:</dt><dd>27</dd><dt>Fuel:</dt><dd>Diesel</dd><dt>Transmission:</dt><dd>Manual</dd><dt>Colour:</dt><dd>White</dd><dt>Berths:</dt><dd>5</dd><dt>Belts:</dt><dd>4</dd><dt>Engine Power:</dt><dd>150 BHP</dd><dt>Length:</dt><dd>7,530</dd><dt>Width:</dt><dd>2,270</dd></dl></div>
    <div class="rv-photo" role="img" aria-label="Photo of a pickup truck with a camper unit"></div>
    <div class="rv-info"><h3>2016 Camper Van 150 BHP</h3><div class="price">$150<small>Per Day</small></div><p>Low Profile, Cab Air Conditioning, Swivel Driver/passenger Seat, Cruise Control, Central Locking, Fine Wood Dashboard Inlays, Rear Garage, Vento Toilet Ventilation, Dvb-t Radio/dvd</p><div class="actions"><span class="btn btn-sky">Schedule Now</span><span class="btn btn-orange">Join the Club</span></div></div>
  </article>

  <article class="rv-card" style="top:708px">
    <div class="specs"><h4>SpecificationS</h4><dl><dt>Mileage:</dt><dd>27</dd><dt>Fuel:</dt><dd>Diesel</dd><dt>Transmission:</dt><dd>Manual</dd><dt>Colour:</dt><dd>White</dd><dt>Berths:</dt><dd>5</dd><dt>Belts:</dt><dd>4</dd><dt>Engine Power:</dt><dd>150 BHP</dd><dt>Length:</dt><dd>7,530</dd><dt>Width:</dt><dd>2,270</dd></dl></div>
    <div class="rv-photo" role="img" aria-label="Photo of a white motorhome with grey trim"></div>
    <div class="rv-info"><h3>2016 Camper Van 150 BHP</h3><div class="price">$150<small>Per Day</small></div><p>Low Profile, Cab Air Conditioning, Swivel Driver/passenger Seat, Cruise Control, Central Locking, Fine Wood Dashboard Inlays, Rear Garage, Vento Toilet Ventilation, Dvb-t Radio/dvd</p><div class="actions"><span class="btn btn-sky">Schedule Now</span><span class="btn btn-orange">Join the Club</span></div></div>
  </article>

  <article class="rv-card" style="top:1008px">
    <div class="specs"><h4>SpecificationS</h4><dl><dt>Mileage:</dt><dd>27</dd><dt>Fuel:</dt><dd>Diesel</dd><dt>Transmission:</dt><dd>Manual</dd><dt>Colour:</dt><dd>White</dd><dt>Berths:</dt><dd>5</dd><dt>Belts:</dt><dd>4</dd><dt>Engine Power:</dt><dd>150 BHP</dd><dt>Length:</dt><dd>7,530</dd><dt>Width:</dt><dd>2,270</dd></dl></div>
    <div class="rv-photo" role="img" aria-label="Side view of a white motorhome"></div>
    <div class="rv-info"><h3>2016 Camper Van 150 BHP</h3><div class="price">$150<small>Per Day</small></div><p>Low Profile, Cab Air Conditioning, Swivel Driver/passenger Seat, Cruise Control, Central Locking, Fine Wood Dashboard Inlays, Rear Garage, Vento Toilet Ventilation, Dvb-t Radio/dvd</p><div class="actions"><span class="btn btn-sky">Schedule Now</span><span class="btn btn-orange">Join the Club</span></div></div>
  </article>

  <article class="rv-card" style="top:1308px">
    <div class="specs"><h4>SpecificationS</h4><dl><dt>Mileage:</dt><dd>27</dd><dt>Fuel:</dt><dd>Diesel</dd><dt>Transmission:</dt><dd>Manual</dd><dt>Colour:</dt><dd>White</dd><dt>Berths:</dt><dd>5</dd><dt>Belts:</dt><dd>4</dd><dt>Engine Power:</dt><dd>150 BHP</dd><dt>Length:</dt><dd>7,530</dd><dt>Width:</dt><dd>2,270</dd></dl></div>
    <div class="rv-photo" role="img" aria-label="Drawing of a pickup truck carrying a camper"></div>
    <div class="rv-info"><h3>2016 Camper Van 150 BHP</h3><div class="price">$150<small>Per Day</small></div><p>Low Profile, Cab Air Conditioning, Swivel Driver/passenger Seat, Cruise Control, Central Locking, Fine Wood Dashboard Inlays, Rear Garage, Vento Toilet Ventilation, Dvb-t Radio/dvd</p><div class="actions"><span class="btn btn-sky">Schedule Now</span><span class="btn btn-orange">Join the Club</span></div></div>
  </article>

  <ul class="pager">
    <li class="wide">Prev</li><li>1</li><li>2</li><li>3</li><li>4</li><li>5</li><li>6</li><li>...</li><li>22</li><li class="wide">Next</li>
  </ul>
</main>

<footer class="site-footer">
  <div class="f-col" style="left:132px">
    <h5>Quick Links</h5>
    <ul class="f-links"><li>Home</li><li>RV Rentals</li><li>Specials</li><li>Policies</li><li>Reviews</li><li>Blog</li><li>Contact &amp; Location</li><li>Request Quote</li></ul>
  </div>
  <div class="f-col f-news">
    <h5>Newsletter</h5>
    <p>Subscribe newsletter to receive the updates direct to your inbox.</p>
    <div class="mail-input"><svg width="12" height="10" viewBox="0 0 24 20"><rect x="1" y="1" width="22" height="18" fill="#333"/><path d="M1 2l11 8 11-8" fill="none" stroke="#fff" stroke-width="2"/></svg>Enter Your Mail Id</div>
    <span class="btn-sub">Subscribe</span>
  </div>
  <div class="f-col f-contact">
    <h5>Contact Us</h5>
    <div class="row"><svg width="10" height="14" viewBox="0 0 20 28"><path fill="#fff" d="M10 0a10 10 0 0 0-10 10c0 7 10 18 10 18s10-11 10-18A10 10 0 0 0 10 0zm0 14a4 4 0 1 1 0-8 4 4 0 0 1 0 8z"/></svg><span>Neque porro quisquam est, qui dolorem ipsum quia dolor</span></div>
    <div class="row"><svg width="12" height="12" viewBox="0 0 24 24"><path fill="#fff" d="M6.6 10.8a15 15 0 0 0 6.6 6.6l2.2-2.2c.3-.3.7-.4 1-.2 1.1.4 2.3.6 3.6.6.6 0 1 .4 1 1V20c0 .6-.4 1-1 1A17 17 0 0 1 3 4c0-.6.4-1 1-1h3.5c.6 0 1 .4 1 1 0 1.3.2 2.5.6 3.6.1.3 0 .7-.2 1z"/></svg><span>1800-555-014</span></div>
    <div class="row"><svg width="12" height="10" viewBox="0 0 24 20"><rect x="1" y="1" width="22" height="18" fill="none" stroke="#fff" stroke-width="2"/><path d="M1 2l11 8 11-8" fill="none" stroke="#fff" stroke-width="2"/></svg><span>desk@birchcoach.example</span></div>
  </div>
  <div class="f-col f-follow">
    <h5>Follow Us</h5>
    <div class="social"><span class="dot"></span>Campfeed</div>
    <div class="social"><span class="dot"></span>Chirper</div>
    <div class="social"><span class="dot"></span>Rss</div>
  </div>
</footer>
<div class="legal"><span>©2016 Birch Coach Rental Club. All Rights Reserved.</span><span>Terms of Use | Privacy Statement &nbsp;|&nbsp; Support</span></div>

</body>
</html>
```